Hip Surgeon needs a web page re-design.

I have a web page to provide information about the diseases of the hip joint for the patients from my private practice since 2008. I need a re-design job for a fresh new look.
We have made a new logo and a new stationery design here in Marqueloft (please see the uploaded files) and I want to make my web page look-alike the new design concepts.
I like the color blue and tones of blue, matching my logo and stationery.
I don't like "busy" designs. It must be clean, elegant and ease to read. The final design should be "mobile friendly" if possible.
Please visit my website www.vilacorendasul.com.br to take a look and get some inspiration.

```html
<!DOCTYPE html>
<html lang="en">
<head>
<meta charset="utf-8">
<title>Dr. Renan T. Calvetti – Cirurgia do Quadril</title>
<link href="https://fonts.googleapis.com/css2?family=Source+Sans+3:ital,wght@0,400;0,600;0,700;1,400&display=swap" rel="stylesheet">
<style>
:root{
  --blue:#1a6cb8;
  --blue-dark:#0d5aa6;
  --blue-light:#2f8fdc;
  --green:#68ab1f;
  --text:#555;
  --muted:#777;
  --footer-top:#676767;
  --footer-bottom:#2c2c2c;
  --footer-text:#e6e6e6;
}
*{box-sizing:border-box;margin:0;padding:0}
html,body{width:748px;height:1200px;overflow:hidden}
body{position:relative;background:#fff;font-family:"Source Sans 3",Arial,sans-serif;color:var(--text)}
.abs{position:absolute}

/* header */
.brand{left:54px;top:32px;display:flex;align-items:center;gap:8px}
.brand-dot{width:56px;height:56px;border-radius:50%;background:var(--blue)}
.brand-name{color:var(--blue);font-weight:400;font-size:21px;line-height:23px}
.search{left:533px;top:50px;width:163px;height:24px;border:1px solid #ccc;font-size:10px;color:#888;padding:5px 8px}
.search svg{position:absolute;right:7px;top:6px}

/* nav */
.nav{left:54px;top:110px;width:644px;height:37px;background:linear-gradient(#2d8ddb,#0f61b3);display:flex}
.nav a{color:#fff;text-decoration:none;font-size:12px;line-height:37px;text-align:center;border-right:1px solid #0c5096;box-shadow:1px 0 0 #3f9be2}
.nav a:last-child{border:none;box-shadow:none;font-weight:600}
.nav a.active{background:linear-gradient(#47a2e6,#1d79c9)}

/* hero */
.hero{left:54px;top:147px;width:644px;height:280px;background:linear-gradient(90deg,#dfe6ec 0%,#eef2f5 45%,#f4f6f8 60%,#dde3e9 100%)}
.hero-photo{position:absolute;right:0;top:0;width:316px;height:280px;background:radial-gradient(ellipse at 55% 40%,#e9d4c4 0%,#f3f3f3 45%,#dfe5ec 100%)}
.hero-title{left:25px;top:74px;font-size:24px;color:var(--blue);font-weight:400}
.hero-text{left:25px;top:112px;width:300px;font-size:9.5px;line-height:15px;color:#555}
.btn{top:158px;height:28px;font-size:12px;color:#fff;line-height:28px;text-align:center}
.btn-blue{left:25px;width:78px;background:linear-gradient(#1f7acb,#0d5aa6)}
.btn-green{left:121px;width:76px;background:linear-gradient(#7cc52a,#5a9a16)}
.dots{left:25px;top:264px;display:flex;gap:3px}
.dots i{width:5px;height:5px;border-radius:50%;background:#444}
.dots i:first-child{background:#fff;border:1px solid #888}

/* diseases */
.section-title{font-size:18px;color:var(--blue);font-weight:400}
.card{top:511px;width:185px}
.card-img{height:93px}
.card h3{font-size:12px;font-weight:400;color:var(--blue);margin-top:9px}
.card p{font-size:8.8px;letter-spacing:-.2px;line-height:15px;color:var(--muted);margin-top:6px;white-space:nowrap}
.divider{left:54px;top:700px;width:644px;height:14px;background:radial-gradient(ellipse at 50% 100%,rgba(0,0,0,.09),rgba(0,0,0,0) 70%)}

/* welcome */
.welcome-photo{left:54px;top:781px;width:130px;height:145px;background:linear-gradient(#eef0f2,#dfe3e7)}
.welcome-body{left:201px;top:790px;width:262px}
.welcome-body h4{font-size:10.5px;line-height:17px;font-weight:400;color:var(--blue);margin-bottom:6px}
.welcome-body p{font-size:9px;letter-spacing:-.1px;line-height:15px;color:#555}

/* testimonials */
.quote{left:504px;top:776px;width:193px;height:78px;background:#f0f0f0;padding:7px 10px 0 16px;font-style:italic;font-size:8.5px;line-height:14px;color:#666}
.quote::after{content:"";position:absolute;right:28px;bottom:-14px;border-left:20px solid transparent;border-top:14px solid #f0f0f0}
.t-photo{left:514px;top:866px;width:68px;height:60px;background:linear-gradient(#cfd6de,#5d6f86)}
.t-role{left:594px;top:876px;width:106px;font-size:8.5px;line-height:12px;font-weight:700;color:#333}
.t-name{left:594px;top:914px;font-size:8.5px;font-weight:700;color:#333;display:flex;gap:6px;align-items:center}

/* footer */
.footer{left:0;top:970px;width:748px;height:230px;background:linear-gradient(var(--footer-top),var(--footer-bottom))}
.f-col h5{font-size:14px;font-weight:400;color:#fff;margin-bottom:2px}
.f-col li{list-style:none;font-size:9.5px;line-height:20.3px;color:var(--footer-text)}
.post{display:flex;gap:7px;font-size:9.5px;line-height:16px;color:var(--footer-text);margin-bottom:8px}
.post em{display:block;font-size:8.5px;color:#fff}
.post i{flex:none;width:9px;height:9px;border-radius:50%;background:#ddd;margin-top:3px}
.map{left:513px;top:1028px;width:184px;height:98px;background:linear-gradient(135deg,#e9e5dc 0%,#cfe0f2 45%,#a9c9ec 60%,#e8e4da 100%)}
.f-rule{left:54px;top:1158px;width:644px;height:1px;background:#777}
.copy{left:54px;top:1176px;font-size:9px;color:#fff}
.social{left:583px;top:1173px;display:flex;gap:5px}
.social i{width:18px;height:18px;border-radius:50%;background:#8a8a8a}
</style>
</head>
<body>

<header>
  <div class="abs brand">
    <span class="brand-dot"></span>
    <span class="brand-name">Dr. Renan T. Calvetti<br>Cirurgia do Quadril</span>
  </div>
  <div class="abs search">Search..
    <svg width="10" height="10" viewBox="0 0 10 10"><circle cx="4" cy="4" r="3" fill="none" stroke="#999" stroke-width="1.4"/><path d="M6.3 6.3 9 9" stroke="#999" stroke-width="1.4"/></svg>
  </div>
</header>

<nav class="abs nav">
  <a class="active" style="width:77px">HOME</a>
  <a style="width:98px">ABOUT US</a>
  <a style="width:69px">LINKS</a>
  <a style="width:99px">OUR BLOG</a>
  <a style="width:114px">DOWNLOADS</a>
  <a style="width:73px">TEAM</a>
  <a style="width:114px">CONTACT US</a>
</nav>

<section class="abs hero">
  <div class="hero-photo" role="img" aria-label="Photo of a smiling doctor in a white coat with a stethoscope in a bright clinic"></div>
  <h1 class="abs hero-title">Claritas est etiam processus</h1>
  <p class="abs hero-text">Nam liber tempor cum solutan nobis eleind option coniue nihil imperdiet doiming iquod mazim placeratfacer possim assumTypi non habent.</p>
  <span class="abs btn btn-blue">Read More</span>
  <span class="abs btn btn-green">Start Here</span>
  <div class="abs dots"><i></i><i></i><i></i><i></i></div>
</section>

<h2 class="abs section-title" style="left:54px;top:472px">Information About the Diseases</h2>
<svg class="abs" style="left:678px;top:478px" width="20" height="12" viewBox="0 0 20 12"><path d="M7 1 2 6l5 5M13 1l5 5-5 5" fill="none" stroke="#888" stroke-width="1.5"/></svg>

<article class="abs card" style="left:54px">
  <div class="card-img" role="img" aria-label="Illustration of a glowing hip joint in the human pelvis" style="background:linear-gradient(120deg,#0a1a6a,#2a6fe0 50%,#f08a2a 60%,#0c2a8a)"></div>
  <h3>Vivamus sagittis lacus</h3>
  <p>Lasodiaer leroas accntium reuekentie riasesa In<br>veveritati etchcto beatae vitae dictiuntaxplic.</p>
</article>
<article class="abs card" style="left:281px">
  <div class="card-img" role="img" aria-label="Illustration of a running leg with a highlighted hip joint" style="background:radial-gradient(ellipse at 45% 45%,#c9641e 0%,#555 30%,#0b0b0b 70%)"></div>
  <h3>Aoreet lacus incididunt</h3>
  <p>Lasodiaer leroas accntium reuekentie riasesa In<br>veveritati etchcto beatae vitae dictiuntaxplic.</p>
</article>
<article class="abs card" style="left:512px">
  <div class="card-img" role="img" aria-label="Model of a pelvis bone with hip joint" style="background:radial-gradient(ellipse at 50% 50%,#dcd9c8 0%,#eeeee8 55%,#fafafa 100%);border:1px solid #ddd"></div>
  <h3>Aoreet lacus incididunt</h3>
  <p>Lasodiaer leroas accntium reuekentie riasesa In<br>veveritati etchcto beatae vitae dictiuntaxplic.</p>
</article>

<div class="abs divider"></div>

<h2 class="abs section-title" style="left:54px;top:748px">Welcome to Our Website</h2>
<div class="abs welcome-photo" role="img" aria-label="Photo of a female doctor with arms crossed and a stethoscope"></div>
<div class="abs welcome-body">
  <h4>TYPI NON HABENT CLARITATEM INSITAM; EST USUS LEGENTIS INIIS QUI FACIT EORUM CLARITATE</h4>
  <p>Claritas est etiam processus dynamicus, qui sequitur mutationem consuetudium lectoum. Mirum est notare quam littera gothica,qu am nunc putamus parum claram, anteposuerit litterarum formash umanitatis per seacula quarta decima et quinta decima. Eodem</p>
  <p style="margin-top:2px">Duis autem vel eum iriure dolor in hendrerit in vulputate velit esse molestie consequat, vel illum dolore eu feugiat nulla facilisis.</p>
</div>

<h2 class="abs section-title" style="left:504px;top:748px">Testimonials</h2>
<blockquote class="abs quote">Fusce feugiat malesuada odio. Morbi nunc do gravida at, cursus nec, luctus a, lorem. Maecn as tristique orci acd sem. Lorem ipsum dolorsi t amet, consectetur adipisicing elit.</blockquote>
<div class="abs t-photo" role="img" aria-label="Portrait photo of a smiling man in a suit"></div>
<p class="abs t-role">Maecenintty interu coquat sit amet, consectetur</p>
<p class="abs t-name"><svg width="10" height="10" viewBox="0 0 10 10"><circle cx="5" cy="3" r="2.5" fill="#555"/><path d="M0 10c0-3 2-4.5 5-4.5S10 7 10 10z" fill="#555"/></svg>Noel Varga</p>

<footer class="abs footer"></footer>
<div class="abs f-col" style="left:54px;top:1001px">
  <h5>LINKS</h5>
  <ul><li>Privacy Policy</li><li>About Us</li><li>Track Order</li><li>Store Locator</li><li>Brand Houses</li><li>Gift Cards</li></ul>
</div>
<div class="abs f-col" style="left:164px;top:1001px">
  <h5>LINKS</h5>
  <ul><li>Privacy Policy</li><li>About Us</li><li>Track Order</li><li>Store Locator</li><li>Brand Houses</li><li>Gift Cards</li></ul>
</div>
<div class="abs f-col" style="left:281px;top:1001px;width:200px">
  <h5 style="margin-bottom:8px">Blog Posts</h5>
  <div class="post"><i></i><span>Linda : Vivamus sagittis lacus vel auguet mfaucibus dolor auctor. Aenean.<em>Posted on March 14, 2014</em></span></div>
  <div class="post"><i></i><span>Linda : Vivamus sagittis lacus vel auguie mfaucibus dolor auctor. Aenean.<em>Posted on March 14, 2014</em></span></div>
</div>
<div class="abs f-col" style="left:513px;top:1001px"><h5>Location</h5></div>
<div class="abs map" role="img" aria-label="Map of the practice location"></div>
<div class="abs f-rule"></div>
<p class="abs copy">Copyright ©2013. All Rights Reserved.</p>
<div class="abs social"><i></i><i></i><i></i><i></i></div>

</body>
</html>
```